Business Card for Pet Food Deliver

Looking for a business card design for a start up company. We are Brisk Hound, Premium Pet Products Brought Round.

We market and are designing a website where our clients can go to and order pet food. We then deliver to a local client base. We do person to person deliver, we do not ship at this point. We are starting off with dog and cat food and treats.

Attached is our logo. We are looking for a fun yet professional design. Eye catching with color but not over the top with color. Looking for a double sided card. Contact info on the front and our logo on the back maybe. . .

I am a huge green fan. However, I am thinking I like the orange a bit more then the blue and green for dominant colors. . .

I am attaching our logo.

The file that has our slogan under has a minor change not implemented yet. The word 'Premium' should be gray to match and the word 'Delivered' should be black to match.

Target Market(s)

We are looking to service those pet owners looking for the convenience of not having to drive to a pet store to purchase their products. We are looking for those who are web savvy and purchase online.

We will also be targeting seniors in senior communities without consistent transprotation.

Industry/Entity Type

Pet

Font styles to use
Sans Serif

Colors
f37122
3176b5
acd036

Requirements
Must have
• Double sided. Logo only on one side with a bold color for the background.

Space for name, phone number, website address, mailing address.
Should not have
• No paws, delivery trucks.

```html
<!DOCTYPE html>
<html lang="en">
<head>
<meta charset="utf-8">
<title>Brisk Hound – Business Card</title>
<link rel="stylesheet" href="https://fonts.googleapis.com/css2?family=Montserrat:wght@400;500;600&display=swap">
<style>
  :root {
    --backdrop: #ececec;
    --card-white: #f7f7f7;
    --brand-orange: #de8a22;
    --brand-green: #8dbf2e;
    --ink-gray: #5f5f5f;
    --logo-white: #ffffff;
    --card-shadow: rgba(0, 0, 0, 0.14);
  }
  * { box-sizing: border-box; margin: 0; padding: 0; }
  html, body {
    width: 1200px;
    height: 900px;
    overflow: hidden;
    background: var(--backdrop);
    font-family: "Montserrat", Arial, sans-serif;
  }
  .card-set {
    position: absolute;
    inset: 0;
    display: flex;
    align-items: center;
    justify-content: center;
    gap: 60px;
  }
  .card {
    position: relative;
    width: 525px;
    height: 300px;
    border-radius: 3px;
    box-shadow: 0 14px 30px var(--card-shadow), 0 2px 4px var(--card-shadow);
  }
  /* Contact side */
  .card--contact {
    background: var(--card-white);
  }
  .contact-person {
    position: absolute;
    right: 38px;
    top: 118px;
    text-align: right;
  }
  .contact-person__name {
    color: var(--brand-green);
    font-weight: 500;
    font-size: 19px;
    letter-spacing: 0.2px;
  }
  .contact-person__role {
    color: var(--ink-gray);
    font-weight: 400;
    font-size: 13px;
    margin-top: 4px;
  }
  .contact-details {
    position: absolute;
    right: 38px;
    bottom: 34px;
    text-align: right;
    font-style: normal;
    color: var(--ink-gray);
    font-size: 14px;
    line-height: 1.5;
  }
  /* Brand side */
  .card--brand {
    background: var(--brand-orange);
  }
  .brand-lockup {
    position: absolute;
    right: 36px;
    bottom: 34px;
    text-align: right;
    color: var(--logo-white);
  }
  .brand-lockup__name {
    font-weight: 400;
    font-size: 46px;
    line-height: 1;
    letter-spacing: -0.5px;
  }
  .brand-lockup__tagline {
    margin-top: 8px;
    font-weight: 400;
    font-size: 10px;
    letter-spacing: 1.2px;
    text-transform: uppercase;
  }
</style>
</head>
<body>
  <main class="card-set">
    <section class="card card--contact" aria-label="Business card, contact side">
      <div class="contact-person">
        <p class="contact-person__name">Owen Hartley</p>
        <p class="contact-person__role">Nutrition Specialist</p>
      </div>
      <address class="contact-details">
        48 Larkfield Lane<br>
        Maplebrook, WI 54000<br>
        555-014-2283<br>
        www.BriskHoundBrings.com
      </address>
    </section>

    <section class="card card--brand" aria-label="Business card, brand side">
      <div class="brand-lockup">
        <p class="brand-lockup__name">Brisk Hound</p>
        <p class="brand-lockup__tagline">Premium Pet Products Brought Round</p>
      </div>
    </section>
  </main>
</body>
</html>
```